Kelbrook Training Australia - Course Brochure Design

Kelbrook Training Australia is a Private Register Training Organisation that delivery accredited training courses to students. These courses are delivery via face to face training and distance education (e.g. elearning).

We are looking to get a template designed via adobe in design that we can use for each of our courses and list the information relevant for each one.

It will need to be around 3 - 4 pages long to be able to fit the information required into the brochure, i have attached some example of other providers course information sheets.

From the examples you'll be able to see that most of the information will remained the same until it gets to the course structure.

I would like it to be kept within our current theme, we are in the middle of upgrading our new website and look (www.kelbrook.com.au/drupal).

I look forward to see what you all come back with.

Reason: Hi everyone, Thanks for submitting your design, I have extended the deadline due to not many designs have been submitted. I will be review and providing feedback on the designed submitted this week and will provide some more information based off the work and direction of the designs submitted. Thanks, Ralph.

Target Market(s)

our target market is business and individuals who would like to undergo training course. This brochure needs to display the require information.

Industry/Entity Type

Education

Requirements
Must have
• The brochure must have a front page with a design to list our company logo and information and the course title.

A call to action must be on every page, e.g. footer to enrol now call kelbok on 1800 392 508 or visit www.kelbrook.com.au

Nice to have
• Some picture to fill the pages would add a nice look

```html
<!DOCTYPE html>
<html lang="en">
<head>
<meta charset="utf-8">
<title>Kelbrook Training Australia – Course Brochure, Page 4</title>
<link rel="stylesheet" href="https://fonts.googleapis.com/css2?family=Fira+Sans:wght@400;500;600;700&display=swap">
<style>
  :root {
    --bg: #c9ced4;
    --paper: #ffffff;
    --gold: #d9a62b;
    --orange: #d9772a;
    --blue: #2e6e9a;
    --navy: #1e3350;
    --footer: #144d6e;
    --heading: #1b5c82;
    --ink: #222629;
    --photo-top: #e7ecef;
    --photo-bottom: #c9cfd3;
  }
  * { box-sizing: border-box; margin: 0; padding: 0; }
  html, body { width: 1200px; height: 900px; overflow: hidden; }
  body {
    background: var(--bg);
    font-family: "Fira Sans", Arial, sans-serif;
    color: var(--ink);
  }
  .page {
    position: absolute;
    left: 320px; top: 35px;
    width: 560px; height: 830px;
    background: var(--paper);
    box-shadow: 0 6px 24px rgba(0,0,0,0.18);
  }
  .colour-band { display: flex; height: 32px; }
  .colour-band span:nth-child(1) { flex: 113; background: var(--gold); }
  .colour-band span:nth-child(2) { flex: 138; background: var(--orange); }
  .colour-band span:nth-child(3) { flex: 140; background: var(--blue); }
  .colour-band span:nth-child(4) { flex: 139; background: var(--navy); }

  .photo-frame {
    position: absolute;
    left: 62px; top: 68px;
    width: 440px; height: 305px;
    border: 6px solid var(--footer);
    background: linear-gradient(180deg, var(--photo-top), var(--photo-bottom));
  }

  .column {
    position: absolute; top: 382px;
    font-size: 9px; line-height: 11.4px;
  }
  .column-left { left: 62px; width: 210px; }
  .column-right { left: 290px; width: 215px; }

  .section-title { color: var(--heading); font-weight: 600; font-size: 9.5px; margin-top: 9px; }
  .column > .section-title:first-child { margin-top: 0; }
  .sub-title { color: var(--heading); font-weight: 600; font-size: 9.5px; margin-top: 6px; }
  .group-title { color: #000; font-weight: 600; font-size: 9.5px; margin-top: 4px; }
  .rules p { margin: 0; }
  .rules p + p.gap { margin-top: 11px; }
  .accent { color: var(--heading); font-weight: 600; }

  .unit { display: grid; grid-template-columns: 68px 1fr; column-gap: 4px; }
  .unit .code { white-space: nowrap; }
  .unit.wrap-code { display: block; }
  .unit.wrap-code .code { margin-right: 18px; }

  .footer {
    position: absolute; left: 0; right: 0; bottom: 0;
    height: 48px;
    background: var(--footer);
    color: #fff;
    font-size: 10.5px; font-weight: 500;
    display: flex; align-items: center;
    padding-left: 62px;
    letter-spacing: 0.2px;
  }
  .footer .page-number { margin-right: 8px; }
  .footer .divider { margin-right: 8px; }
</style>
</head>
<body>
  <article class="page">
    <div class="colour-band"><span></span><span></span><span></span><span></span></div>

    <div class="photo-frame" role="img" aria-label="Photo of four business people in light suits smiling around a meeting table in a bright office"></div>

    <section class="column column-left">
      <div class="rules">
        <p class="section-title">Packaging Rules</p>
        <p class="accent">Total number of units = 13</p>
        <p><b>2 core units</b> plus</p>
        <p><b>11 elective</b> units</p>
        <p><b>7 elective units</b> must be selected from the <b>Group A</b> units listed below.</p>
        <p class="gap">The remaining <b>4 elective units</b> may be selected from the <b>Group A</b> or <b>Group B</b> elective units listed below, or any currently endorsed Training Package or accredited course at the same qualification level. If not listed below <b>2 of the electives units</b> may be selected from a Certificate II or Certificate IV qualification.</p>
      </div>

      <p class="section-title">Core Units</p>
      <p class="sub-title">IT Use</p>
      <div class="unit wrap-code"><span class="code">BSBITU307A</span> Develop keyboarding speed and accuracy</div>

      <p class="section-title">Occupational Health and Safety</p>
      <div class="unit"><span class="code">BSBOHS201A</span><span>Participate in OHS processes</span></div>

      <p class="section-title">Elective units</p>
      <p class="sub-title">Group A units</p>
      <p class="sub-title" style="margin-top:0">Financial Administration</p>
      <div class="unit"><span class="code">BSBFIA302A</span><span>Process payroll</span></div>
      <div class="unit"><span class="code">BSBFIA303A</span><span>Process accounts payable and receivable</span></div>
      <div class="unit"><span class="code">BSBFIA304A</span><span>Maintain a general ledger</span></div>

      <p class="section-title">General Administration</p>
      <div class="unit"><span class="code">BSBADM307B</span><span>Organise schedules</span></div>
    </section>

    <section class="column column-right">
      <p class="section-title">IT Use</p>
      <div class="unit"><span class="code">BSBITU302B</span><span>Create electronic presentations</span></div>
      <div class="unit"><span class="code">BSBITU303A</span><span>Design and produce text documents</span></div>
      <div class="unit"><span class="code">BSBITU304A</span><span>Produce spreadsheets</span></div>
      <div class="unit"><span class="code">BSBITU306A</span><span>Design and produce business documents</span></div>
      <div class="unit"><span class="code">BSBITU309A</span><span>Produce desktop published documents</span></div>

      <p class="section-title">Writing</p>
      <div class="unit"><span class="code">BSBWRT301A</span><span>Write simple documents</span></div>

      <p class="section-title">Group B units</p>
      <p class="group-title">Customer Service</p>
      <div class="unit wrap-code"><span class="code">BSBCUS301B</span> Deliver and monitor a service to customers</div>
      <p class="group-title">Diversity</p>
      <div class="unit"><span class="code">BSBDIV301A</span><span>Work effectively with diversity</span></div>
      <p class="group-title">Financial Administration</p>
      <div class="unit"><span class="code">BSBFIA301A</span><span>Maintain financial records</span></div>
      <p class="group-title">General Administration</p>
      <div class="unit"><span class="code">BSBADM302B</span><span>Produce texts from notes</span></div>
      <div class="unit wrap-code"><span class="code">BSBADM303B</span> Produce texts from audio transcription</div>
      <div class="unit"><span class="code">BSBADM311A</span><span>Maintain business resources</span></div>
      <p class="group-title">Information Management</p>
      <div class="unit"><span class="code">BSBINM301A</span><span>Organise workplace information</span></div>
      <div class="unit"><span class="code">BSBINM302A</span><span>Utilise a knowledge management system</span></div>
      <div class="unit"><span class="code">BSBINM303A</span><span>Handle receipt and despatch of information</span></div>
    </section>

    <footer class="footer">
      <span class="page-number">4</span><span class="divider">|</span>
      <span>To enrol now call kelbok on 1800 392 508 or visit www.kelbrook.com.au</span>
    </footer>
  </article>
</body>
</html>
```